banner add update

I need a banner design for my asbestos company please see my flyer I want this edited I want the company logo at the top kept put to the left of the banner and all the txt put into the middle in the same font and the map on the right ! please leave the pic of the person in yellow out !
I need it done asap !
This need to go on 2.5 long and 800 high meter banner so the pixels must be right !
first in first served ! easy money

```html
<!DOCTYPE html>
<html lang="en">
<head>
<meta charset="utf-8">
<title>Ridgeline Asbestos Removal – Banner</title>
<link rel="stylesheet" href="https://fonts.googleapis.com/css2?family=Alfa+Slab+One&family=Open+Sans:wght@700&family=PT+Sans&family=PT+Sans+Narrow&display=swap">
<style>
  :root {
    --frame-green: #1f7a3e;
    --brand-green: #1d7a34;
    --icon-dark: #2f4a2c;
    --heading-grey: #3f4a42;
    --text-dark: #1b1b1b;
    --signal-yellow: #f6ec1c;
    --paper: #ffffff;
    --map-land: #e6eed6;
    --map-forest: #c9dcae;
    --map-coverage: rgba(120, 200, 190, 0.35);
    --map-sea: #b7dcef;
  }
  * { box-sizing: border-box; margin: 0; padding: 0; }
  html, body { width: 1200px; height: 381px; overflow: hidden; background: var(--paper); }
  .banner {
    position: relative;
    width: 1200px;
    height: 381px;
    background: var(--paper);
    border: 19px solid var(--frame-green);
  }
  .brand {
    position: absolute;
    left: 18px;
    top: 24px;
    width: 432px;
    text-align: center;
    font-family: "Alfa Slab One", serif;
    color: var(--brand-green);
    line-height: 1;
  }
  .brand__top { display: block; font-size: 56px; letter-spacing: 1px; }
  .brand__bottom { display: block; font-size: 35px; margin-top: 12px; letter-spacing: 0.5px; }
  .service-tiles {
    position: absolute;
    left: 25px;
    top: 152px;
    display: flex;
    gap: 14px;
  }
  .service-tile {
    width: 132px;
    height: 157px;
    border: 3px solid var(--brand-green);
    border-radius: 12px;
    background:
      radial-gradient(ellipse 46% 40% at 50% 55%, rgba(47, 74, 44, 0.55) 0%, rgba(47, 74, 44, 0.25) 55%, rgba(47, 74, 44, 0) 100%),
      var(--signal-yellow);
  }
  .details {
    position: absolute;
    left: 450px;
    top: 20px;
    width: 420px;
    text-align: center;
  }
  .details__heading {
    font-family: "Open Sans", sans-serif;
    font-weight: 700;
    font-size: 33px;
    color: var(--heading-grey);
    letter-spacing: 0.5px;
  }
  .details__phone {
    font-family: "Alfa Slab One", serif;
    font-size: 60px;
    color: var(--signal-yellow);
    -webkit-text-stroke: 2px var(--brand-green);
    letter-spacing: 1px;
    line-height: 1.1;
  }
  .details__contact {
    font-family: "PT Sans", sans-serif;
    font-size: 20px;
    color: var(--text-dark);
    line-height: 30px;
    margin-top: 14px;
  }
  .details__points {
    list-style: none;
    font-family: "PT Sans Narrow", sans-serif;
    font-size: 23px;
    color: var(--text-dark);
    line-height: 30px;
    margin-top: 4px;
  }
  .details__points li::before { content: "• "; }
  .coverage-map {
    position: absolute;
    left: 865px;
    top: 25px;
    width: 262px;
    height: 290px;
    border: 3px solid var(--brand-green);
    background:
      radial-gradient(circle at 60% 50%, var(--map-coverage) 0%, var(--map-coverage) 58%, rgba(120, 200, 190, 0) 60%),
      radial-gradient(ellipse 40% 55% at 35% 45%, var(--map-forest) 0%, rgba(201, 220, 174, 0) 100%),
      linear-gradient(100deg, var(--map-land) 0%, var(--map-land) 74%, var(--map-sea) 84%, var(--map-sea) 100%);
  }
</style>
</head>
<body>
  <main class="banner">
    <div class="brand">
      <span class="brand__top">RIDGELINE</span>
      <span class="brand__bottom">ASBESTOS REMOVAL</span>
    </div>

    <div class="service-tiles">
      <div class="service-tile" role="img" aria-label="Icon of a tipper truck"></div>
      <div class="service-tile" role="img" aria-label="Icon of a respirator gas mask"></div>
      <div class="service-tile" role="img" aria-label="Icon of an excavator"></div>
    </div>

    <section class="details">
      <h1 class="details__heading">ASBESTOS REMOVAL</h1>
      <p class="details__phone">0412638175</p>
      <p class="details__contact">ridgelinewasteremoval@example.com<br>www.ridgelinewasteremoval.com</p>
      <ul class="details__points">
        <li>Work cover Accredited</li>
        <li>Fully Licensed</li>
        <li>Comprehensively Insured</li>
      </ul>
    </section>

    <div class="coverage-map" role="img" aria-label="Map of the coastal service area with a circle marking the coverage region"></div>
  </main>
</body>
</html>
```